Business Card design for construction company

I would like a business card design for a construction company - ORD Builders. I have attached the ai logo file for use. I would like the card to be very smart and clean and incorporate only white and the two colours in the logo. I would like the card to have two sides. One side can just have the logo, the other with the relevant information.

Target Market(s)

Building and Construction Clients

Industry/Entity Type

Business

Contact Information for Business Card

Name: Tom Harcliffe
Company: ORD Builders Pty Limited
Address: 14 Mulberry Crescent Oakvale Heights 2093
Phone: 0432 517 208
Email: tomh@ordbuilders.example.au

Font styles to use
Serif
Sans Serif

Requirements
Must have
• Details noted above
• Logo as provided
• Colours as in logo
• Square edges
• A font that compliments the logo
Should not have
• Any colour other than white and those in logo
• Rounded edges

```html
<!DOCTYPE html>
<html lang="en">
<head>
<meta charset="utf-8">
<title>ORD Builders – Business Card</title>
<link href="https://fonts.googleapis.com/css2?family=Open+Sans:wght@400;600;700&display=swap" rel="stylesheet">
<style>
  :root {
    --page: #e6e7e9;
    --card: #fbf9f8;
    --blue: #1aa3e0;
    --grey: #4a4a4c;
    --ink: #3d3d3f;
  }
  * { box-sizing: border-box; margin: 0; padding: 0; }
  html, body {
    width: 1200px; height: 944px; overflow: hidden;
    background: var(--page);
    font-family: "Open Sans", Arial, sans-serif;
  }
  .sheet {
    position: relative; width: 1200px; height: 944px;
    display: flex; flex-direction: column; align-items: center; justify-content: center; gap: 64px;
  }
  .card {
    position: relative; width: 600px; height: 343px;
    background: var(--card);
    box-shadow: 0 6px 18px rgba(0,0,0,.12);
  }
  .card .frame { position: absolute; inset: 0; width: 100%; height: 100%; }

  /* Front */
  .brand {
    position: absolute; left: 0; right: 0; top: 50%; transform: translateY(-50%);
    display: flex; align-items: center; justify-content: center; gap: 12px;
  }
  .brand-mark { width: 14px; height: 14px; background: var(--blue); }
  .brand-name {
    font-weight: 600; font-size: 26px; letter-spacing: 3px; color: var(--ink);
    text-transform: uppercase;
  }

  /* Back */
  .holder {
    position: absolute; right: 62px; top: 88px; text-align: right;
  }
  .holder-name {
    font-weight: 700; font-size: 22px; letter-spacing: 1px; color: var(--ink); text-transform: uppercase;
  }
  .holder-company { font-size: 15px; color: var(--blue); margin-top: 2px; }

  .contact {
    position: absolute; left: 62px; bottom: 96px; list-style: none;
    display: flex; flex-direction: column; gap: 10px;
  }
  .contact li { display: flex; align-items: center; gap: 12px; font-size: 13px; font-weight: 600; color: var(--blue); }
  .contact .icon {
    width: 24px; height: 24px; border-radius: 50%; background: var(--blue);
    display: flex; align-items: center; justify-content: center; flex: none;
  }
  .contact .icon svg { width: 14px; height: 14px; }
</style>
</head>
<body>
<main class="sheet">

  <section class="card card-front" aria-label="Business card front">
    <svg class="frame" viewBox="0 0 600 343" aria-hidden="true">
      <g stroke="var(--blue)" stroke-width="4" fill="none">
        <line x1="0" y1="26" x2="395" y2="26"/>
        <line x1="48" y1="0" x2="48" y2="255"/>
        <line x1="205" y1="317" x2="600" y2="317"/>
        <line x1="552" y1="88" x2="552" y2="343"/>
      </g>
    </svg>
    <div class="brand">
      <span class="brand-mark"></span>
      <span class="brand-name">ORD Builders</span>
    </div>
  </section>

  <section class="card card-back" aria-label="Business card back">
    <svg class="frame" viewBox="0 0 600 343" aria-hidden="true">
      <g stroke="var(--grey)" stroke-width="4" fill="none">
        <line x1="0" y1="38" x2="600" y2="38" stroke-width="0"/>
        <line x1="42" y1="0" x2="42" y2="343"/>
        <line x1="0" y1="300" x2="330" y2="300"/>
        <line x1="558" y1="0" x2="558" y2="343"/>
        <line x1="270" y1="43" x2="600" y2="43"/>
      </g>
    </svg>

    <div class="holder">
      <p class="holder-name">Tom Harcliffe</p>
      <p class="holder-company">ORD Builders Pty Limited</p>
    </div>

    <ul class="contact">
      <li>
        <span class="icon">
          <svg viewBox="0 0 24 24"><path fill="#fff" d="M6.6 10.8a15.1 15.1 0 0 0 6.6 6.6l2.2-2.2c.3-.3.7-.4 1-.2 1.1.4 2.3.6 3.6.6.6 0 1 .4 1 1V20c0 .6-.4 1-1 1A17 17 0 0 1 3 4c0-.6.4-1 1-1h3.5c.6 0 1 .4 1 1 0 1.3.2 2.5.6 3.6.1.3 0 .7-.2 1z"/></svg>
        </span>
        0432 517 208
      </li>
      <li>
        <span class="icon">
          <svg viewBox="0 0 24 24"><rect x="3" y="6" width="18" height="12" fill="#fff"/><path d="M3 6l9 7 9-7" stroke="#1aa3e0" stroke-width="1.6" fill="none"/></svg>
        </span>
        tomh@ordbuilders.example.au
      </li>
      <li>
        <span class="icon">
          <svg viewBox="0 0 24 24"><path fill="#fff" d="M12 2a7 7 0 0 0-7 7c0 5.2 7 13 7 13s7-7.8 7-13a7 7 0 0 0-7-7zm0 9.5A2.5 2.5 0 1 1 12 6.5a2.5 2.5 0 0 1 0 5z"/></svg>
        </span>
        14 Mulberry Crescent Oakvale Heights 2093
      </li>
    </ul>
  </section>

</main>
</body>
</html>
```